business card for dental office

We need a business card design for an existing company follwing information we need on the card:
Tarvek L Osumbe, DDS
4526 Quillmere Court
Springfield, VA 22987
Ph: 703-555-0142 Fax:703-555-0187
www.grinvalemont.com info@grinvalemont.com
second side
Appointment
For
Date: day:
Time
if you are unable to keep your appointment, please contact us 24 hours in advance.
Note: Logo is attached to use with the card
Thanks
Industry/Entity Type
Dental Clinic
Contact Information for Business Card
Tarvek L Osumbe, DDS
4526 Quillmere Court
Springfield, VA 22987
second side
Appointment
For
Date: day:
Time
Thanks

```html
<!DOCTYPE html>
<html lang="en">
<head>
<meta charset="utf-8">
<title>Grinvale Dental Associates – Business Card</title>
<link href="https://fonts.googleapis.com/css2?family=Crimson+Text:ital,wght@0,400;0,700;1,400&family=PT+Sans+Narrow&family=Open+Sans&family=Oswald:wght@400&display=swap" rel="stylesheet">
<style>
  :root {
    --page-bg: #a9a6a7;
    --card-white: #ffffff;
    --card-cream: #f7f4e7;
    --navy: #24528f;
    --brand-blue: #2a4f8c;
    --sky: #2aa9dc;
    --rule: #3f66a3;
    --ink-white: #ffffff;
  }
  * { margin: 0; padding: 0; box-sizing: border-box; }
  html, body { width: 1200px; height: 1200px; overflow: hidden; }
  body { background: var(--page-bg); position: relative; font-family: "Crimson Text", serif; }

  .card { position: absolute; width: 712px; border-radius: 22px; overflow: hidden; }
  .card--appointment { left: 238px; top: 118px; height: 419px; background: var(--card-white); }
  .card--contact { left: 230px; top: 644px; height: 417px; background: var(--card-cream); }

  .brand-name {
    position: absolute; left: 0; width: 100%; text-align: center;
    font-family: "Crimson Text", serif; font-weight: 700; font-size: 44px;
    color: var(--brand-blue); line-height: 1;
  }
  .card--appointment .brand-name { top: 100px; }
  .card--contact .brand-name { top: 100px; }

  .appointment-title {
    position: absolute; top: 218px; width: 100%; text-align: center;
    font-family: "Crimson Text", serif; font-weight: 700; font-size: 21px;
    letter-spacing: 0.5px; color: var(--brand-blue);
  }
  .field { position: absolute; font-family: "PT Sans Narrow", sans-serif; font-size: 20px; color: var(--brand-blue); line-height: 1; }
  .rule { position: absolute; height: 1.5px; background: var(--rule); }

  .notice-band {
    position: absolute; left: 0; bottom: 0; width: 100%; height: 45px;
    background: var(--navy); color: var(--ink-white);
    font-family: "Open Sans", sans-serif; font-size: 15.5px;
    display: flex; align-items: center; justify-content: center;
  }

  .contact-wave { position: absolute; left: 0; top: 0; width: 712px; height: 417px; }

  .person { position: absolute; right: 399px; top: 283px; text-align: right; color: var(--ink-white); }
  .person-name { font-family: "Oswald", sans-serif; font-size: 23px; line-height: 1.15; }
  .person-title { font-style: italic; font-size: 16px; margin-top: 1px; }
  .person-address { font-size: 17px; line-height: 23px; margin-top: 4px; }

  .contact-list { position: absolute; left: 340px; top: 282px; list-style: none; }
  .contact-list li { display: flex; align-items: center; height: 26.5px; color: var(--ink-white); font-size: 21px; }
  .contact-list svg { width: 20px; height: 20px; margin-right: 20px; fill: var(--sky); }
</style>
</head>
<body>

  <section class="card card--appointment">
    <div class="brand-name">Grinvale Dental Associates</div>
    <h2 class="appointment-title">YOUR APPOINTMENT</h2>

    <span class="field" style="left:34px; top:255px;">For</span>
    <div class="rule" style="left:60px; top:276px; width:619px;"></div>

    <div class="rule" style="left:34px; top:313px; width:416px;"></div>
    <span class="field" style="left:450px; top:292px;">Day:</span>
    <div class="rule" style="left:486px; top:313px; width:193px;"></div>

    <span class="field" style="left:34px; top:329px;">Date</span>
    <div class="rule" style="left:70px; top:350px; width:281px;"></div>
    <span class="field" style="left:357px; top:329px;">Time:</span>
    <div class="rule" style="left:398px; top:350px; width:281px;"></div>

    <div class="notice-band">if you are unable to keep your appointment, please contact us 24 hours in advance</div>
  </section>

  <section class="card card--contact">
    <div class="brand-name">Grinvale Dental Associates</div>

    <svg class="contact-wave" viewBox="0 0 712 417" aria-hidden="true">
      <path d="M0,276 Q356,196 712,276 L712,417 L0,417 Z" fill="var(--navy)"/>
      <path d="M-5,268 Q356,176 717,268" fill="none" stroke="var(--sky)" stroke-width="5"/>
    </svg>

    <div class="person">
      <div class="person-name">Tarvek L Osumbe</div>
      <div class="person-title">DDS</div>
      <div class="person-address">4526 Quillmere Court<br>Springfield, VA 22987</div>
    </div>

    <ul class="contact-list">
      <li><svg viewBox="0 0 20 20" aria-label="Phone"><path d="M2 6c0-2 3-3 8-3s8 1 8 3v2h-4V6H6v2H2z"/><path d="M5 9h10l2 8H3z"/><circle cx="10" cy="13" r="2" fill="var(--navy)"/></svg>703-555-0142</li>
      <li><svg viewBox="0 0 20 20" aria-label="Fax"><rect x="5" y="2" width="10" height="5"/><rect x="2" y="7" width="16" height="8" rx="2"/><rect x="5" y="12" width="10" height="6" stroke="var(--navy)" stroke-width="1"/></svg>703-555-0187</li>
      <li><svg viewBox="0 0 20 20" aria-label="Email"><rect x="2" y="4" width="16" height="12"/><path d="M2 4l8 7 8-7" fill="none" stroke="var(--navy)" stroke-width="1.5"/></svg>info@grinvalemont.com</li>
      <li><svg viewBox="0 0 20 20" aria-label="Website"><circle cx="10" cy="10" r="8"/><path d="M2 10h16M10 2v16M4 6h12M4 14h12" stroke="var(--navy)" stroke-width="1" fill="none"/><ellipse cx="10" cy="10" rx="3.5" ry="8" fill="none" stroke="var(--navy)" stroke-width="1"/></svg>www.grinvalemont.com</li>
    </ul>
  </section>

</body>
</html>
```